Business Card Design Project

We are looking for a new business card design for a Drilling company in WA, Australia.

We are in between offices, however require a design in the meantime due to some upcoming events with our basic information.

The Logo for our company is Blue and Grey and would like this colour scheme throughout.

We are quite a new company so would like a memorable design that stands out and communicates a strong commitment to safety, quality of work and performance.

The company name is Ironbark Boring Group (IBG)

The details to be included are as follows:

Gavin Thorley
Managing Director
m.0481639207
e.gavin@ibgpty.com.au

Martin Thorley
Director
m.0419852637
e.martin@ibgpty.com.au

Industry/Entity Type

Events

Requirements
Must have
• Under the Logo, we would like 'Western Australia'

```html
<!DOCTYPE html>
<html lang="en">
<head>
<meta charset="utf-8">
<title>Ironbark Boring Group – Business Cards</title>
<link rel="stylesheet" href="https://fonts.googleapis.com/css2?family=Arimo:wght@400;700&display=swap">
<style>
  :root {
    --navy: #062f66;
    --navy-line: #0b3a78;
    --grey-text: #9c9c9c;
    --grey-light: #d6d6d6;
    --grey-dark: #7d7d7d;
    --white: #ffffff;
    --stage-dark: #b3b3b3;
    --stage-light: #f2f2f2;
  }
  * { margin: 0; padding: 0; box-sizing: border-box; }
  html, body { width: 1200px; height: 900px; overflow: hidden; }
  body {
    position: relative;
    font-family: "Arimo", Arial, sans-serif;
    background: linear-gradient(110deg, var(--stage-dark) 0%, #cfcfcf 55%, var(--stage-light) 100%);
  }
  .card {
    position: absolute;
    width: 594px;
    height: 396px;
    background: var(--white);
    overflow: hidden;
  }
  .card--front { left: 43px; top: 39px; }
  .card--back { left: 513px; top: 464px; }
  .card-art { position: absolute; inset: 0; width: 100%; height: 100%; }
  .brand {
    position: absolute;
    text-align: center;
    color: var(--navy);
  }
  .card--front .brand { left: 60px; top: 42px; width: 340px; }
  .card--back .brand { left: 128px; top: 148px; width: 340px; }
  .brand-name {
    display: flex;
    align-items: center;
    justify-content: center;
    gap: 10px;
    font-size: 29px;
    font-weight: 700;
    letter-spacing: 0.5px;
    white-space: nowrap;
  }
  .brand-mark {
    width: 18px; height: 18px;
    background: var(--navy);
  }
  .brand-region {
    margin-top: 14px;
    font-size: 12.5px;
    letter-spacing: 3.2px;
  }
  .ghost-initials {
    position: absolute;
    left: 255px; top: 180px;
    font-size: 170px;
    font-weight: 700;
    color: var(--navy-line);
    opacity: 0.55;
    line-height: 1;
  }
  .contact {
    position: absolute;
    top: 236px;
    width: 240px;
    text-align: center;
  }
  .contact--left { left: 40px; }
  .contact--right { left: 281px; }
  .contact-name { font-size: 28px; color: var(--grey-text); line-height: 1.05; }
  .contact-role { font-size: 19px; color: var(--grey-text); line-height: 1.1; }
  .contact-mobile { font-size: 19px; color: var(--white); margin-top: 8px; }
  .contact-email { font-size: 16.5px; color: var(--white); margin-top: 6px; }
</style>
</head>
<body>

<section class="card card--front" aria-label="Business card front">
  <svg class="card-art" viewBox="0 0 594 396" aria-hidden="true">
    <defs>
      <linearGradient id="swooshFront" x1="0" y1="0" x2="1" y2="0">
        <stop offset="0" stop-color="#e2e2e2"/>
        <stop offset="1" stop-color="#747474"/>
      </linearGradient>
    </defs>
    <path d="M0,152 C130,210 400,205 492,116 L594,116 L594,396 L0,396 Z" fill="var(--navy)"/>
    <path d="M0,98 C70,150 390,168 492,110 C420,186 130,200 0,146 Z" fill="url(#swooshFront)"/>
  </svg>
  <div class="brand">
    <div class="brand-name"><span class="brand-mark"></span>Ironbark Boring Group</div>
    <div class="brand-region">Western Australia</div>
  </div>
  <div class="ghost-initials" aria-hidden="true">IBG</div>
  <div class="contact contact--left">
    <p class="contact-name">Gavin Thorley</p>
    <p class="contact-role">Managing Director</p>
    <p class="contact-mobile">m.0481639207</p>
    <p class="contact-email">e.gavin@ibgpty.com.au</p>
  </div>
  <div class="contact contact--right">
    <p class="contact-name">Martin Thorley</p>
    <p class="contact-role">Director</p>
    <p class="contact-mobile">m.0419852637</p>
    <p class="contact-email">e.martin@ibgpty.com.au</p>
  </div>
</section>

<section class="card card--back" aria-label="Business card back">
  <svg class="card-art" viewBox="0 0 594 396" aria-hidden="true">
    <defs>
      <linearGradient id="swooshBack" x1="0" y1="0" x2="1" y2="0">
        <stop offset="0" stop-color="#e2e2e2"/>
        <stop offset="1" stop-color="#747474"/>
      </linearGradient>
    </defs>
    <g transform="translate(0,164)">
      <path d="M0,152 C130,210 400,205 492,116 L594,116 L594,396 L0,396 Z" fill="var(--navy)"/>
      <path d="M0,98 C70,150 390,168 492,110 C420,186 130,200 0,146 Z" fill="url(#swooshBack)"/>
    </g>
  </svg>
  <div class="brand">
    <div class="brand-name"><span class="brand-mark"></span>Ironbark Boring Group</div>
    <div class="brand-region">Western Australia</div>
  </div>
</section>

</body>
</html>
```